Stationary Design to Complement our Website

We would like template designed for word documents that we can use for headed paper. The template should complement the style of our website & incorporate our existing logo. https://www.velmorantravel.com/

The header and footer design should be sperate PNG or JPEG files that we can copy and paste into word header and footers. They should work on A4 & letter sized papers.

Note the main web colours are as follows:

Black
HEX code #2b2c2b
C=71 M=64 Y=64 K=65
RGB 43,44,43

Green
HEX code #116c49
C=88 M=33 Y=82 K=24
RGB 17,108,73

Current fonts are ALEO & Gilroy.

Fonts and colours in new design don't have to match website exactly but should be complementary.

Font styles to use
Serif

Requirements
Must have
• a simple design that complements our website.
Some kind of graphic on the top & some sort of graphic on the bottom. Not just plain logo on top.
designs that incorporate the clouds might look good
Can also incorporate 5* rate harbor rating
Should not have
• no photographs included on the design

```html
<!DOCTYPE html>
<html lang="en">
<head>
<meta charset="utf-8">
<title>Velmoran Travel — Letterhead</title>
<link rel="stylesheet" href="https://fonts.googleapis.com/css2?family=Cinzel:wght@400&family=Lato:wght@400&family=Montserrat:wght@300;800&family=PT+Sans+Narrow:wght@400&display=swap">
<style>
  :root {
    --brand-green: #116c49;
    --ink: #2b2c2b;
    --text-grey: #555657;
    --muted-grey: #666867;
    --backdrop: #d9d9d9;
    --paper: #ffffff;
    --signature-tint: #e4efe9;
  }
  * { margin: 0; padding: 0; box-sizing: border-box; }
  html, body { width: 1056px; height: 1200px; overflow: hidden; }
  body { background: var(--backdrop); position: relative; }

  .letterhead {
    position: absolute; left: 104px; top: 0;
    width: 848px; height: 1200px;
    background: var(--paper);
    overflow: hidden;
  }

  /* Header */
  .brand {
    position: absolute; left: 80px; top: 58px;
    display: flex; align-items: flex-start; gap: 10px;
  }
  .brand-dot { width: 14px; height: 14px; border-radius: 50%; background: var(--brand-green); margin-top: 6px; }
  .brand-name {
    font-family: "Cinzel", serif; font-weight: 400; color: var(--ink);
    font-size: 32px; line-height: 48px; letter-spacing: 7px;
  }
  .brand-name span { display: block; }
  .brand-name .first { padding-left: 8px; }

  .contact {
    position: absolute; right: 80px; top: 55px;
    font-family: "Lato", sans-serif; font-size: 15px; color: var(--muted-grey);
    text-align: right; line-height: 19px;
  }
  .contact .address { margin-bottom: 9px; }
  .contact .line { display: flex; justify-content: flex-end; align-items: center; gap: 12px; height: 22px; }
  .contact svg { width: 15px; height: 15px; flex: none; }

  .header-rule {
    position: absolute; left: 80px; top: 180px; width: 687px; height: 1.5px;
    background: var(--brand-green);
  }

  /* Letter body */
  .letter { position: absolute; left: 80px; top: 428px; width: 688px; }
  .date { font-family: "Montserrat", sans-serif; font-weight: 300; font-size: 19px; color: var(--text-grey); }
  .recipient-name {
    font-family: "Montserrat", sans-serif; font-weight: 800; font-size: 29px;
    color: var(--text-grey); margin-top: 8px; letter-spacing: 0.3px;
  }
  .recipient-role { font-family: "Montserrat", sans-serif; font-weight: 300; font-size: 19px; color: var(--text-grey); margin-top: 4px; }

  .body-copy {
    font-family: "PT Sans Narrow", sans-serif; font-size: 17px; color: var(--text-grey);
    line-height: 29.5px; text-align: justify; margin-top: 48px;
  }
  .body-copy p + p { margin-top: 29.5px; }

  .sign-off { font-family: "PT Sans Narrow", sans-serif; font-size: 19px; color: var(--text-grey); margin-top: 56px; }
  .signature {
    width: 90px; height: 56px; margin-top: 22px; border-radius: 4px;
    background: linear-gradient(135deg, var(--signature-tint), #f3f8f5);
  }

  /* Footer */
  .footer-band {
    position: absolute; left: 0; bottom: 0; width: 100%; height: 16px;
    background: var(--brand-green);
  }
</style>
</head>
<body>
  <main class="letterhead">
    <header>
      <div class="brand">
        <div class="brand-dot"></div>
        <div class="brand-name"><span class="first">Velmoran</span><span>Travel</span></div>
      </div>

      <address class="contact" style="font-style:normal">
        <div class="address">Alder Court, Brookfield Lane,<br>Glenmore East, Co. Westport, Ireland</div>
        <div class="line">+353 (0)61 40218
          <svg viewBox="0 0 16 16" aria-hidden="true"><path d="M4 1.5 6.2 4.6 4.9 6.2c.8 1.9 2.4 3.6 4.4 4.6l1.6-1.4 3.1 2.2-1.3 2.5c-5.6-.4-10.4-5.4-10.7-11z" fill="var(--brand-green)"/><path d="M9.5 2.5a4 4 0 0 1 4 4M9.5.5a6 6 0 0 1 6 6" stroke="var(--brand-green)" stroke-width="1.3" fill="none"/></svg>
        </div>
        <div class="line">hello@velmorantravel.com
          <svg viewBox="0 0 16 16" aria-hidden="true"><rect x="1" y="3" width="14" height="10" fill="var(--brand-green)"/><path d="M1 3.5 8 9l7-5.5M1 12.5l5-4.5M15 12.5l-5-4.5" stroke="#fff" stroke-width="1.1" fill="none"/></svg>
        </div>
        <div class="line">www.velmorantravel.com
          <svg viewBox="0 0 16 16" aria-hidden="true"><g stroke="var(--brand-green)" stroke-width="1.1" fill="none"><circle cx="8" cy="8" r="6.5"/><ellipse cx="8" cy="8" rx="3" ry="6.5"/><path d="M1.5 8h13M2.5 4.8h11M2.5 11.2h11"/></g></svg>
        </div>
      </address>

      <div class="header-rule"></div>
    </header>

    <section class="letter">
      <p class="date">10 December, 2021</p>
      <h1 class="recipient-name">DANIEL HARTLEY</h1>
      <p class="recipient-role">Cheif Executive Officer</p>

      <div class="body-copy">
        <p>Contrary to popular belief, Lorem Ipsum is not simply random text. It has roots in a piece of classical Latin literature from 45 BC, making it over 2000 years old. Edwin Marlowe, a Latin professor at Ashgrove College in Vermont, looked up one of the more obscure Latin words, consectetur.</p>
        <p>Lorem Ipsum comes from sections 1.10.32 and 1.10.33 of "de Finibus Bonorum et Malorum" (The Extremes of Good and Evil) by Aurelius Varro, written in 45 BC. This book is a treatise on the theory of ethics, very popular during the Renaissance. The first line of Lorem Ipsum.</p>
        <p>The standard chunk of Lorem Ipsum used since the 1500s is reproduced below for those interested.</p>
      </div>

      <p class="sign-off">Best Regards</p>
      <div class="signature" role="img" aria-label="Handwritten signature of the sender in green ink"></div>
    </section>

    <footer class="footer-band"></footer>
  </main>
</body>
</html>
```